Halcott Business Card Design

Photography business needs a logo. I would like to see creative licence on options on 1 & 2 sided. I really like the concept of a fully / partially frosted design. I have already used ArtisanHive for my Logo, so I am looking for the same level of assistance with this project.

Industry/Entity Type

Business

Font styles to use
Serif
Script

Requirements
Must have
• Must Have:
• - These are my contact details
• Name: Ames K Halcott
• Mobile: 5550193827
• email: lenorapaske@fernpost.net

```html
<!DOCTYPE html>
<html lang="en">
<head>
<meta charset="utf-8">
<title>Halcott Business Card</title>
<link rel="stylesheet" href="https://fonts.googleapis.com/css2?family=Arimo&family=Carlito&family=Gelasio&display=swap">
<style>
  :root {
    --bg-start: #1489c5;
    --bg-mid: #2a7392;
    --bg-end: #3f5963;
    --bracket: #3ba8c9;
    --placeholder-ink: #33302e;
    --name-ink: #efefef;
    --contact-ink: #e2e8eb;
  }
  html, body {
    margin: 0;
    padding: 0;
    overflow: hidden;
    background: var(--bg-end);
  }
  .card {
    position: relative;
    width: 1200px;
    height: 540px;
    overflow: hidden;
    background: linear-gradient(105deg, var(--bg-start) 0%, var(--bg-mid) 50%, var(--bg-end) 100%);
  }
  .logo-frame {
    position: absolute;
    left: 455px;
    top: 87px;
    width: 290px;
    height: 178px;
  }
  .logo-frame svg {
    position: absolute;
    inset: 0;
  }
  .logo-placeholder {
    position: absolute;
    left: 0;
    right: 0;
    top: 146px;
    margin: 0;
    text-align: center;
    font-family: "Arimo", sans-serif;
    font-size: 52px;
    line-height: 64px;
    color: var(--placeholder-ink);
  }
  .owner-name {
    position: absolute;
    left: 0;
    right: 0;
    top: 304px;
    margin: 0;
    text-align: center;
    font-family: "Gelasio", serif;
    font-weight: 400;
    font-size: 146px;
    line-height: 170px;
    color: var(--name-ink);
    white-space: nowrap;
  }
  .owner-role {
    position: absolute;
    left: 0;
    right: 0;
    top: 453px;
    margin: 0;
    text-align: center;
    font-family: "Carlito", sans-serif;
    font-size: 49px;
    line-height: 60px;
    letter-spacing: 1px;
    color: var(--name-ink);
  }
  .contact {
    position: absolute;
    bottom: 20px;
    margin: 0;
    font-family: "Carlito", sans-serif;
    font-size: 20px;
    line-height: 24px;
    letter-spacing: 0.5px;
    color: var(--contact-ink);
  }
  .contact-mobile { left: 30px; }
  .contact-email { right: 30px; }
</style>
</head>
<body>
  <main class="card">
    <div class="logo-frame">
      <svg width="290" height="178" viewBox="0 0 290 178" aria-hidden="true">
        <path d="M110 6 H6 V172 H110" fill="none" stroke="var(--bracket)" stroke-width="12"/>
        <path d="M180 6 H284 V172 H180" fill="none" stroke="var(--bracket)" stroke-width="12"/>
      </svg>
    </div>
    <p class="logo-placeholder">Logo Here</p>
    <h1 class="owner-name">Ames K Halcott</h1>
    <p class="owner-role">Photographer</p>
    <p class="contact contact-mobile">M: 5550193827</p>
    <p class="contact contact-email">lenorapaske@fernpost.net</p>
  </main>
</body>
</html>
```